Business Card Design Project

Im an electrician and my company name is Kestrel Electrical
My main work is installing Lighting and Power Points, Home Theater Systems, TVS, Phones and Data
Im looking a business card, something nice, clean, modern and not to cluttered
Im open to sugestions
I dont mind if the "Services" is on the back on the business card
colours black, grey, white or the blue colour of my logo are prefered but not compulsory
any questions just message me
and please make it so if i need to edit the writing can do it easy. maybe by making it a seperate layer ?
My Details are.
Name - Peter Halloran
Job Title - Licenced Electrician
Mobile - 027 583 2174
Email - peter@kestrelelectrical.co.nz
Web - www.kestrelelectrical.co.nz
Services
Residential / Commercial
Lighting & Power
Heating & Ventilation
Automation
Phone & Data
Home Cinema
Sound Systems
TV, Antenna & Satellite
Digital Upgrades

```html
<!DOCTYPE html>
<html lang="en">
<head>
<meta charset="utf-8">
<title>Kestrel Electrical – Business Card</title>
<link rel="stylesheet" href="https://fonts.googleapis.com/css2?family=Open+Sans:wght@400;600;700&display=swap">
<style>
  :root {
    --page-bg: #2b2b2d;
    --brand-blue: #1c9bb0;
    --card-black: #0e0e0f;
    --silver-light: #f4f4f4;
    --silver-mid: #cfcfd1;
    --silver-dark: #9d9ea1;
    --ink: #1a1a1a;
    --white: #ffffff;
  }
  * { box-sizing: border-box; margin: 0; padding: 0; }
  html, body {
    width: 1200px;
    height: 900px;
    overflow: hidden;
    background: var(--page-bg);
    font-family: "Open Sans", Arial, sans-serif;
  }
  .canvas {
    position: relative;
    width: 1200px;
    height: 900px;
  }
  .presentation-title {
    position: absolute;
    top: 30px;
    right: 46px;
    color: var(--white);
    font-size: 50px;
    font-weight: 400;
    letter-spacing: -0.5px;
  }
  .card {
    position: absolute;
    top: 290px;
    width: 540px;
    height: 310px;
    border-radius: 22px;
    overflow: hidden;
    box-shadow: 0 14px 30px rgba(0,0,0,0.45);
  }
  .brand {
    position: absolute;
    top: 34px;
    left: 40px;
    display: flex;
    align-items: center;
    gap: 10px;
  }
  .brand-mark {
    width: 30px;
    height: 30px;
    background: var(--brand-blue);
  }
  .brand-name {
    color: var(--brand-blue);
    font-weight: 700;
    font-size: 19px;
    line-height: 1;
    letter-spacing: 0.5px;
    text-transform: uppercase;
  }

  /* Front: silver */
  .card-front {
    left: 40px;
    background: linear-gradient(160deg, var(--silver-light) 0%, #dcdcde 45%, var(--silver-mid) 75%, #e9e9ea 100%);
  }
  .card-front .sheen-lines {
    position: absolute;
    left: 0;
    right: 0;
    top: 80px;
    height: 150px;
    background: repeating-linear-gradient(180deg, rgba(255,255,255,0.75) 0 3px, transparent 3px 20px);
    opacity: 0.5;
  }
  .contact {
    position: absolute;
    right: 40px;
    bottom: 44px;
    text-align: right;
    color: var(--ink);
  }
  .contact-name { font-size: 17px; font-weight: 700; }
  .contact-role { font-size: 12px; margin-bottom: 18px; }
  .contact-line { font-size: 14px; line-height: 1.5; }
  .contact-line b { font-weight: 700; }

  /* Back: black with service stripes */
  .card-back {
    right: 40px;
    background: var(--card-black);
  }
  .services {
    position: absolute;
    top: 76px;
    left: 150px;
    right: 0;
    list-style: none;
  }
  .service {
    height: 19px;
    margin-bottom: 2px;
    padding-right: 26px;
    text-align: right;
    font-size: 14px;
    line-height: 19px;
    color: var(--ink);
    background: linear-gradient(90deg, rgba(150,150,152,0) 0%, var(--silver-dark) 25%, var(--silver-mid) 55%, var(--silver-light) 100%);
  }
  .web {
    position: absolute;
    right: 26px;
    bottom: 14px;
    color: var(--white);
    font-size: 17px;
    font-weight: 700;
    line-height: 1.3;
  }
</style>
</head>
<body>
<main class="canvas">
  <h1 class="presentation-title">Kestrel Electrical</h1>

  <section class="card card-front" aria-label="Card front">
    <div class="sheen-lines"></div>
    <div class="brand">
      <span class="brand-mark"></span>
      <span class="brand-name">Kestrel Electrical</span>
    </div>
    <div class="contact">
      <p class="contact-name">Peter Halloran</p>
      <p class="contact-role">Licenced Electrician</p>
      <p class="contact-line"><b>M</b> 027 583 2174</p>
      <p class="contact-line"><b>E</b> peter@kestrelelectrical.co.nz</p>
    </div>
  </section>

  <section class="card card-back" aria-label="Card back">
    <div class="brand">
      <span class="brand-mark"></span>
      <span class="brand-name">Kestrel Electrical</span>
    </div>
    <ul class="services">
      <li class="service">Automation</li>
      <li class="service">Phone &amp; Data</li>
      <li class="service">Home Cinema</li>
      <li class="service">Sound Systems</li>
      <li class="service">Digital Upgrades</li>
      <li class="service">Lighting &amp; Power</li>
      <li class="service">Heating &amp; Ventilation</li>
      <li class="service">TV, Antenna &amp; Satellite</li>
      <li class="service">Residential / Commercial</li>
    </ul>
    <p class="web">www.kestrelelectrical.co.nz</p>
  </section>
</main>
</body>
</html>
```